Refresh of far beyond ordinary IT house website

Our web site is starting to show it's age. You can see the existing site here: www.plumbrook.net. As a growing company we want to come across as a dynamic collection of IT experts.

We want to update the design so are open to any colour palette and look, but want to retain our current table logo. We use the logo on our business cards but with a white background - see the attached file, so you don't need to keep the brown or the green.

The design should consider the range of browsers that will be looking at the site - so please show how it will look on a wide screen laptop and a 768x1024 tablet.

We want to add some pages about our team and their skills, probably with photos of each person on the team.

This is an uncoded project - the PSD files of the design is required, not coding.
Updates

Thanks everyone for the submissions so far.  It's a holiday day in the UK today but we will get some feedback on the designs so far out to you.

Target Market(s)

Architects and other creative types looking for IT support

Industry/Entity Type

Business

Font styles to use
Serif
Sans Serif

Requirements
Must have
• Must look good on a laptop and an iPad.

```html
<!DOCTYPE html>
<html lang="en">
<head>
<meta charset="utf-8">
<title>plumbrook – IT support for business</title>
<link rel="stylesheet" href="https://fonts.googleapis.com/css2?family=Roboto:wght@300;400;500&display=swap">
<style>
:root{
  --plum:#8e1052;
  --gold:#d6aa00;
  --ink:#333;
  --muted:#8a8a8a;
  --soft:#f3f3f3;
  --rule:#d9d9d9;
  --footer:#3c3c3c;
  --white:#fff;
}
*{box-sizing:border-box;margin:0;padding:0}
html,body{width:722px;height:1200px;overflow:hidden}
body{font-family:"Roboto",sans-serif;color:var(--ink);background:var(--white);position:relative}
a{color:inherit;text-decoration:none}

.site-header{height:70px;position:relative}
.brand{position:absolute;left:50px;top:24px;display:flex;align-items:center;gap:8px;color:var(--plum);font-size:19px;font-weight:500}
.brand-mark{width:20px;height:20px;background:var(--gold)}
.remote{position:absolute;right:37px;top:32px;display:flex;align-items:center;font-size:10px;color:var(--muted)}
.remote-label{margin-right:8px}
.remote-input{width:112px;height:16px;background:#c9c9c9;color:#e9e9e9;font-size:8px;padding:3px 5px}
.remote-go{width:21px;height:16px;background:var(--gold);color:var(--white);font-size:8px;font-weight:500;margin-left:3px;display:flex;align-items:center;justify-content:center}

.main-nav{height:31px;background:var(--plum);display:flex;padding-left:38px}
.main-nav a{color:var(--white);font-size:9px;display:flex;align-items:center;padding:0 12px;border-right:1px solid rgba(255,255,255,.25)}
.main-nav a:last-child{border-right:0}
.main-nav a.is-active{background:var(--gold);padding:0 14px}

.hero{position:absolute;left:4px;top:101px;width:718px;height:324px;background:linear-gradient(90deg,#c9c9c9 0%,#e4e6e8 35%,#f0f0f0 70%,#ececec 100%)}
.hero-photo{position:absolute;left:0;top:0;width:470px;height:324px;background:linear-gradient(120deg,#b8b8b8,#e0e2e4 55%,rgba(236,236,236,0))}
.hero-copy{position:absolute;left:470px;top:88px;width:222px}
.hero-kicker{font-size:19px;color:#555;font-weight:400;letter-spacing:.2px}
.hero-title{font-size:23px;color:var(--plum);font-weight:500;margin-top:2px}
.hero-text{font-size:10px;line-height:13px;color:#666;margin-top:12px}
.btn-gold{display:inline-block;background:var(--gold);color:var(--white);font-size:10px;padding:9px 14px;margin-top:14px}
.hero-dots{position:absolute;right:50px;top:300px;display:flex;gap:7px}
.hero-dots i{width:6px;height:6px;border-radius:50%;background:#b5b5b5}
.hero-dots i.is-on{background:var(--plum)}

.services{position:absolute;left:39px;top:460px;display:flex;gap:9px}
.service{width:122px;text-align:center}
.service-title{height:30px;font-size:12px;font-weight:400;color:#222;display:flex;align-items:center;justify-content:center;line-height:13px}
.service-img{height:95px;margin-top:4px}
.service-text{font-size:8.5px;line-height:10.5px;color:#9a9a9a;font-weight:300;margin-top:6px;padding:0 3px}
.btn-plum{display:inline-block;background:var(--plum);color:var(--white);font-size:9px;padding:4px 11px}
.service .btn-plum{margin-top:11px}

.info{position:absolute;left:0;top:697px;width:722px;height:268px;background:var(--soft);border-top:1px solid #e5e5e5}
.info-col{position:absolute;top:14px;height:240px}
.info-col h2{font-size:24px;font-weight:300;color:#444;margin-top:16px}
.welcome{left:40px;width:180px}
.welcome p{font-size:10px;line-height:15px;color:#666;font-weight:300;margin-top:20px}
.welcome .btn-plum{margin-top:40px}
.news{left:230px;width:228px;border-left:1px solid var(--rule);border-right:1px solid var(--rule);padding-left:12px;padding-right:12px}
.news-item{padding:10px 0 9px;border-bottom:1px dotted #c6c6c6}
.news-item:last-child{border-bottom:0}
.news-item h3,.article h3{font-size:9px;font-weight:400;color:var(--plum);line-height:11px}
.news-item p,.article p{font-size:7px;line-height:9px;color:var(--muted);margin-top:4px}
.news h2{margin-bottom:14px}
.articles{left:470px;width:212px}
.articles h2{margin-bottom:17px}
.article{display:flex;gap:8px;margin-bottom:30px}
.article-img{width:45px;height:45px;flex:none}

.partners{position:absolute;left:0;top:965px;width:722px;height:121px;display:flex;align-items:center;justify-content:center}
.partners .arrow{color:#aaa;font-size:20px;font-weight:300;width:50px;text-align:center}
.partner{width:97px;text-align:center;font-size:15px;font-weight:500;color:#555}

.site-footer{position:absolute;left:0;top:1086px;width:722px;height:114px;background:var(--footer)}
.footer-nav{position:absolute;left:41px;top:25px;font-size:8.5px;color:#bdbdbd}
.footer-nav span{margin:0 4px;color:#888}
.copyright{position:absolute;left:41px;top:46px;font-size:8px;color:#777}
.social{position:absolute;left:41px;top:66px;display:flex;gap:5px}
.social i{width:24px;height:24px;border-radius:50%;background:#5a5a5a;border:1px solid #6b6b6b}
.footer-brand{position:absolute;right:40px;top:40px;display:flex;align-items:center;gap:8px;font-size:19px;font-weight:500;color:#222}
.footer-brand .brand-mark{background:#222}
</style>
</head>
<body>
<header class="site-header">
  <a class="brand" href="#"><span class="brand-mark"></span>plumbrook</a>
  <div class="remote"><span class="remote-label">Remote</span><span class="remote-input">Session ID</span><span class="remote-go">GO</span></div>
</header>
<nav class="main-nav">
  <a class="is-active" href="#">HOME</a><a href="#">ABOUT US</a><a href="#">WHAT WE DO</a><a href="#">NEWS BLOG</a><a href="#">ARTICLES</a><a href="#">CLIENTS</a><a href="#">PARTNERS</a><a href="#">CONTACT</a><a href="#">SUPPORT</a><a href="#">TERMS</a>
</nav>

<section class="hero">
  <div class="hero-photo" role="img" aria-label="Two business people shaking hands across a desk with a laptop in a bright office"></div>
  <div class="hero-copy">
    <p class="hero-kicker">SERIOUS IT SUPPORT</p>
    <h1 class="hero-title">FOR BUSINESS</h1>
    <p class="hero-text">Aenean massa. Cum sociis natoque penatibus et magnis dis parturient montes, nascetur ridiculus mus. Donec quam felis, ultricies nec, pellentesque eu, pretium quis, sem. Nulla consequat massa quis enim.</p>
    <a class="btn-gold" href="#">KNOW MORE</a>
  </div>
  <div class="hero-dots"><i class="is-on"></i><i></i><i></i><i></i></div>
</section>

<section class="services">
  <div class="service"><h3 class="service-title">IT Support &amp;<br>Management</h3><div class="service-img" role="img" aria-label="Hands joining coloured puzzle pieces" style="background:linear-gradient(135deg,#9a9a9a,#c4553a 45%,#3f8f3a 70%,#7a7a7a)"></div><p class="service-text">Aenean vulputate eleifend tellus. Aenean leo ligula, porttitor eu, consequat vitae, eleifend ac, enim.</p><a class="btn-plum" href="#">Read More</a></div>
  <div class="service"><h3 class="service-title">Cloud Computing</h3><div class="service-img" role="img" aria-label="Blue cloud computing network illustration" style="background:linear-gradient(135deg,#0d3a6e,#1f7cc0 55%,#0b2f5c)"></div><p class="service-text">Aenean vulputate eleifend tellus. Aenean leo ligula, porttitor eu, consequat vitae, eleifend ac, enim.</p><a class="btn-plum" href="#">Read More</a></div>
  <div class="service"><h3 class="service-title">Disaster Recovery</h3><div class="service-img" role="img" aria-label="Hand pressing a recover button on a blue screen" style="background:linear-gradient(135deg,#1d4f9a,#2e6cc0 55%,#163f7e)"></div><p class="service-text">Aenean vulputate eleifend tellus. Aenean leo ligula, porttitor eu, consequat vitae, eleifend ac, enim.</p><a class="btn-plum" href="#">Read More</a></div>
  <div class="service"><h3 class="service-title">Virtualisation</h3><div class="service-img" role="img" aria-label="Abstract teal digital rings" style="background:linear-gradient(90deg,#0e4f6a,#1597b8 55%,#5fcbe0)"></div><p class="service-text">Aenean vulputate eleifend tellus. Aenean leo ligula, porttitor eu, consequat vitae, eleifend ac, enim.</p><a class="btn-plum" href="#">Read More</a></div>
  <div class="service"><h3 class="service-title">Cad Services</h3><div class="service-img" role="img" aria-label="Blue architectural wireframe of a building" style="background:linear-gradient(135deg,#1a3f9e,#2f5fc8 55%,#14348a)"></div><p class="service-text">Aenean vulputate eleifend tellus. Aenean leo ligula, porttitor eu, consequat vitae, eleifend ac, enim.</p><a class="btn-plum" href="#">Read More</a></div>
</section>

<section class="info">
  <div class="info-col welcome">
    <h2>Welcome</h2>
    <p>Plumbrook was established with a specific aim: to consistently deliver an advanced and comprehensive IT service for ambitious growing companies across all industry sectors.</p>
    <a class="btn-plum" href="#">Read More</a>
  </div>
  <div class="info-col news">
    <h2>Latest News</h2>
    <div class="news-item"><h3>Plumbrook launch phone and tablet apps</h3><p>Consistently deliver an advanced and comprehensive IT service for ambitious growing</p></div>
    <div class="news-item"><h3>Plumbrook launch phone and tablet apps</h3><p>Consistently deliver an advanced and comprehensive IT service for ambitious growing</p></div>
    <div class="news-item"><h3>Plumbrook launch phone and tablet apps</h3><p>Consistently deliver an advanced and comprehensive IT service for ambitious growing</p></div>
  </div>
  <div class="info-col articles">
    <h2>Latest Articles</h2>
    <div class="article"><div class="article-img" role="img" aria-label="Blue cloud icon on a screen" style="background:linear-gradient(135deg,#1c7fc4,#5fb5e8)"></div><div><h3>Plumbrook launch phone and tablet apps</h3><p>Consistently deliver an advanced and comprehensive IT service for ambitious growing. Consistently deliver a comprehensive IT service for ambitious growing</p></div></div>
    <div class="article"><div class="article-img" role="img" aria-label="Support agent wearing a headset" style="background:linear-gradient(135deg,#d8c8b8,#f2f2f2)"></div><div><h3>Plumbrook launch phone and tablet apps</h3><p>Consistently deliver an advanced and comprehensive IT service for ambitious growing. Consistently deliver a comprehensive IT service for ambitious growing</p></div></div>
  </div>
</section>

<section class="partners">
  <span class="arrow">&#10216;</span>
  <span class="partner">Corevia</span>
  <span class="partner">Lumisoft</span>
  <span class="partner">Datanest</span>
  <span class="partner">Orbiquel</span>
  <span class="partner">Shieldon</span>
  <span class="partner">Telvara</span>
  <span class="arrow">&#10217;</span>
</section>

<footer class="site-footer">
  <nav class="footer-nav">About us<span>|</span>What we do<span>|</span>News blog<span>|</span>Articles<span>|</span>Clients<span>|</span>Partners<span>|</span>Contact<span>|</span>Support<span>|</span>Terms</nav>
  <p class="copyright">All Rights Reserved. Copyrights @ 2014</p>
  <div class="social"><i></i><i></i><i></i><i></i></div>
  <div class="footer-brand"><span class="brand-mark"></span>plumbrook</div>
</footer>
</body>
</html>
```